Letterhead Design for Law Firm

**Edit: I have added the photo of a bottom that I like.

------
We are looking for a re-design of our new letterhead. The letterhead is for a law firm and will be used for digital and traditionally printed correspondence.

Here are some suggestions:

- Please use colours are #8ec900 and simple black.
- Please do not use any type of "waves" at the bottom of the page. This is not in style at all.
- Please stay modern yet conservative.
- Please use font Segoe UI Light or similar if you can
- Avoid clipart or illustrations.
- Utilize ample white space in the layout so the design looks clean and information is easy to read at a glance. Don't overcrowd the letterhead.
- Make sure the letterhead design is consistent with our brand identity (see brambleford.ca)
-Please, no black headers or footers.

I am attaching my current letterhead and signature for your convenience.

Remember, the letterhead is an extension of our professional identity. We are a successful firm and trial lawyers who correspond with insurers, judges, lawyers, courts, clients, etc. Make it new, modern, attractive, yet powerful and conservative.

It needs to be easily printable. I would like the bleed removed in print so the black bar the bottom crosses the page (but the text is not near the edges)

Target Market(s)

Clients, Government Offices, Judiciary, Lawyers, Insurance Companies, Colleagues.

Industry/Entity Type

Law

Font styles to use
Other font styles liked:
• Segoe UI LIght, Calibri Light,

Colors
00AB8E
00BBA5
67D7C9
C6EFE9
E9F9F6

Requirements
Must have
• Everything that is on the letterhead now.
Nice to have
• Cutting Edge design, yet conservative.
Should not have
• law firm cliche design, images,

```html
<!DOCTYPE html>
<html lang="en">
<head>
<meta charset="utf-8">
<title>Merridew Letterhead</title>
<link rel="stylesheet" href="https://fonts.googleapis.com/css2?family=Open+Sans:wght@400&display=swap">
<style>
  :root {
    --backdrop: #d4d4d4;
    --paper: #ffffff;
    --ink: #1a1a1a;
    --accent: #8ec900;
  }
  * { margin: 0; padding: 0; box-sizing: border-box; }
  html, body {
    width: 1200px;
    height: 848px;
    overflow: hidden;
    background: var(--backdrop);
    font-family: "Open Sans", sans-serif;
  }
  .canvas {
    position: relative;
    width: 1200px;
    height: 848px;
    display: flex;
    align-items: center;
    justify-content: center;
  }
  .letterhead {
    position: relative;
    width: 618px;
    height: 800px;
    background: var(--paper);
    box-shadow: 0 2px 10px rgba(0, 0, 0, 0.15);
  }
  .letterhead__brand {
    position: absolute;
    top: 52px;
    left: 48px;
    font-size: 34px;
    font-weight: 400;
    letter-spacing: 2px;
    color: var(--ink);
    line-height: 1;
  }
  .letterhead__footer {
    position: absolute;
    left: 0;
    right: 0;
    bottom: 44px;
    text-align: center;
    font-size: 11.5px;
    line-height: 1.45;
    color: var(--ink);
  }
  .letterhead__separator {
    display: inline-block;
    width: 4px;
    height: 4px;
    margin: 0 5px 2px;
    border-radius: 50%;
    background: var(--accent);
    vertical-align: middle;
  }
</style>
</head>
<body>
  <main class="canvas">
    <article class="letterhead">
      <header class="letterhead__brand">MERRIDEW</header>
      <footer class="letterhead__footer">
        <p class="letterhead__address">48 Alder Row, Suite 1210, Fenwick, ON K2V 3B7, Canada</p>
        <p class="letterhead__contact">555-014-2290<span class="letterhead__separator"></span>info@brambleford.ca</p>
        <p class="letterhead__web">www.brambleford.ca</p>
      </footer>
    </article>
  </main>
</body>
</html>
```